Supplment jar label design (full label)

Hydration (blue) 300g –700ml jar, label size: 10 cm x 27 cm
make label for Dr Quillo supps
needs to be full blown label that fits size I noted above
with all claims in attached doc
see attached product info and claims
see KLT & Ember attached as example of similar to what I want
carbon fibre background on label
I have also attached label example this is how i expect to receive designs
where is states SKU on label needs to be in colour above
needs files to able to customise with other SKUs in future
please message me if you have questions
Hydration

```html
<!DOCTYPE html>
<html lang="en">
<head>
<meta charset="utf-8">
<title>Dr Quillo Hydration – Full Label</title>
<link href="https://fonts.googleapis.com/css2?family=Bebas+Neue&family=Montserrat:wght@300;400;600;700&family=Arimo:wght@400;700&display=swap" rel="stylesheet">
<style>
  :root {
    --page: #ffffff;
    --label-dark: #0b0c0d;
    --label-mid: #1c1e20;
    --brand-white: #f4f4f4;
    --sku-blue: #1ba0e2;
    --wave-deep: #0a3d7a;
    --wave-bright: #3fb3ff;
    --panel-white: #ffffff;
    --ink: #111111;
    --body-text: #e9e9e9;
    --muted: #bdbdbd;
  }
  * { margin: 0; padding: 0; box-sizing: border-box; }
  html, body { width: 960px; height: 1200px; overflow: hidden; background: var(--page); }
  .canvas { position: relative; width: 960px; height: 1200px; }

  .label {
    position: absolute; left: 36px; top: 430px; width: 890px; height: 330px;
    background: radial-gradient(ellipse at 52% 45%, var(--label-mid) 0%, var(--label-dark) 70%);
    color: var(--body-text); font-family: "Arimo", Arial, sans-serif;
    overflow: hidden;
  }

  /* left information column */
  .info { position: absolute; left: 31px; top: 44px; width: 200px; font-size: 7.8px; line-height: 1.28; }
  .info p { margin-bottom: 14px; }
  .info .key { color: var(--sku-blue); font-weight: 700; }
  .info .site { color: var(--sku-blue); font-weight: 700; font-size: 10.5px; margin-top: 18px; }

  /* decorative wave area */
  .wave { position: absolute; left: 246px; top: 0; width: 100px; height: 330px; }

  /* centre front panel */
  .front { position: absolute; left: 356px; top: 0; width: 240px; height: 330px; }
  .brand {
    position: absolute; left: 0; top: 92px;
    font-family: "Montserrat", Arial, sans-serif; font-weight: 700; color: var(--brand-white);
    font-size: 32px; line-height: 1; letter-spacing: 1px; white-space: nowrap;
  }
  .sku {
    position: absolute; left: 0; top: 186px;
    font-family: "Bebas Neue", Impact, sans-serif; color: var(--sku-blue);
    font-size: 60px; line-height: 1; letter-spacing: 0.5px;
  }
  .descriptor { position: absolute; left: 4px; top: 256px; font-family: "Montserrat", sans-serif; font-weight: 700; font-size: 8.6px; letter-spacing: 0.6px; color: var(--brand-white); white-space: nowrap; }
  .flavour { position: absolute; left: 46px; top: 277px; font-family: "Montserrat", sans-serif; font-weight: 300; font-size: 8.4px; letter-spacing: 0.6px; color: var(--muted); }
  .pack-row { position: absolute; left: 0; top: 291px; display: flex; align-items: center; font-family: "Montserrat", sans-serif; color: var(--brand-white); }
  .servings-count { border: 1.5px solid var(--brand-white); font-weight: 700; font-size: 19px; line-height: 1; padding: 1px 2px; }
  .servings-word { font-size: 12.5px; letter-spacing: 0.8px; margin-left: 3px; }
  .net { margin-left: 26px; text-align: center; line-height: 1.05; }
  .net small { display: block; font-size: 7.8px; }
  .net strong { font-weight: 400; font-size: 11px; }

  /* nutrition panel */
  .nutrition { position: absolute; left: 632px; top: 48px; width: 226px; font-size: 7.6px; }
  .nip { background: var(--panel-white); color: var(--ink); border: 1px solid var(--ink); }
  .nip h2 { font-family: "Arimo", sans-serif; font-weight: 400; font-size: 14.5px; letter-spacing: 0.4px; line-height: 1; padding: 1px 2px 0; border-bottom: 1px solid var(--ink); }
  .nip .serve { padding: 1px 3px; border-bottom: 1px solid var(--ink); font-size: 6.8px; }
  .nip table { width: 100%; border-collapse: collapse; }
  .nip td, .nip th { border-right: 1px solid var(--ink); padding: 0 2px; text-align: left; font-weight: 400; line-height: 1.3; }
  .nip td:last-child, .nip th:last-child { border-right: none; }
  .nip th { font-size: 6.6px; line-height: 1.1; border-bottom: 1px solid var(--ink); vertical-align: top; }
  .nip .col-name { width: 32%; }
  .nip .col-serve { width: 36%; }
  .nip tr.row td { border-bottom: 1px solid #999; }
  .nip tr.row:last-child td { border-bottom: none; }
  .nip-note { margin-top: 5px; color: #cfcfcf; font-size: 7.4px; }
  .claims { margin-top: 12px; line-height: 1.3; font-size: 7.7px; color: var(--body-text); }
  .claim-last { display: flex; align-items: flex-end; justify-content: space-between; }
  .origin-badge { width: 72px; height: 18px; background: var(--panel-white); border: 1px solid #3a3a3a; }
</style>
</head>
<body>
<div class="canvas">
  <section class="label" aria-label="Dr Quillo Hydration full wrap label">
    <div class="info">
      <p><span class="key">Ingredients:</span> Electrolyte Minerals (Sodium Chloride, Magnesium Chloride, Potassium Chloride, Calcium Citrate), Acacia Gum, Natural Flavouring, Food Acid (Citric Acid), Sweetener (Thaumatin^). ^Katemfe Fruit Extract</p>
      <p><span class="key">Directions:</span> Add 10g (approx. 2 scoops) into 500ml of chilly water depending on your liking, stir or shake to dissolve.<br>Store below 30°C in a cool, dry place.</p>
      <p><span class="key">Recommended Daily Intake:</span> 1 serving.</p>
      <p>Formulated Supplementary Sports Food.<br>This product is not a sole source of nutrition and should be consumed in conjunction with a nutritious diet and an appropriate physical training or exercise program.<br>*Not suitable for children under 15 years of age or pregnant women: Should only be used under medical or dietetic supervision.</p>
      <div class="site">drquillo.example</div>
    </div>

    <svg class="wave" viewBox="0 0 100 330" role="img" aria-label="Flowing blue smoke wave artwork">
      <defs>
        <linearGradient id="waveFill" x1="0" y1="0" x2="1" y2="1">
          <stop offset="0" stop-color="#0a3d7a" stop-opacity="0.9"/>
          <stop offset="0.5" stop-color="#3fb3ff" stop-opacity="0.75"/>
          <stop offset="1" stop-color="#0a3d7a" stop-opacity="0.6"/>
        </linearGradient>
      </defs>
      <rect x="0" y="0" width="100" height="330" fill="url(#waveFill)" opacity="0.55"/>
    </svg>

    <div class="front">
      <div class="brand">DR QUILLO</div>
      <div class="sku">HYDRATION</div>
      <div class="descriptor">ADVANCED ELECTROLYTE BLEND</div>
      <div class="flavour">LEMON FLAVOUR</div>
      <div class="pack-row">
        <span class="servings-count">30</span>
        <span class="servings-word">SERVINGS</span>
        <span class="net"><small>Net WT</small><strong>300g</strong></span>
      </div>
    </div>

    <div class="nutrition">
      <div class="nip">
        <h2>NUTRITION INFORMATION</h2>
        <div class="serve">Servings per package: 30 Serving size: 10g</div>
        <table>
          <tr>
            <th class="col-name"></th>
            <th class="col-serve">AVERAGE QUANTITY PER SERVING</th>
            <th>AVERAGE QUANTITY PER 100g</th>
          </tr>
          <tr class="row"><td>Energy</td><td>34.6 kJ (8.3 Cal)</td><td>346 kJ (83 Cal)</td></tr>
          <tr class="row"><td>Protein</td><td>0.1 g</td><td>1.1 g</td></tr>
          <tr class="row"><td>-Gluten</td><td>Nil detected</td><td>Nil detected</td></tr>
          <tr class="row"><td>Fat, Total</td><td>0.0 g</td><td>0.0 g</td></tr>
          <tr class="row"><td>-Saturated</td><td>0.0 g</td><td>0.0 g</td></tr>
          <tr class="row"><td>Carbohydrate</td><td>0.0 g</td><td>0.0 g</td></tr>
          <tr class="row"><td>-Sugars</td><td>0.0 g</td><td>0.0 g</td></tr>
          <tr class="row"><td>Dietary Fibre</td><td>3.9 g</td><td>39.0 g</td></tr>
          <tr class="row"><td>Sodium</td><td>1,200 mg</td><td>12,000 mg</td></tr>
          <tr class="row"><td>Potassium</td><td>250 mg</td><td>2,500 mg</td></tr>
          <tr class="row"><td>Calcium</td><td>80 mg</td><td>800 mg</td></tr>
          <tr class="row"><td>Magnesium</td><td>80 mg</td><td>800 mg</td></tr>
        </table>
      </div>
      <div class="nip-note">Nutrition Information relates to powder only.</div>
      <div class="claims">
        Recommended nutritional claims based on FSANZ Schedule 4:<br>
        1. Gluten Free.<br>
        2. No added artificial flavour, colour &amp; sweetener.<br>
        3. Potassium is necessary for normal water and electrolyte balance.
        <div class="claim-last">
          <span>4. No Added Sugar</span>
          <span class="origin-badge" aria-hidden="true"></span>
        </div>
      </div>
    </div>
  </section>
</div>
</body>
</html>
```